Business card and stationary for a Massage Therapist
Kneading Haven Studio
Business card and stationary for a Massage Therapist - Massage Therapy
Creative Brief
Professional
Gwen Holloway M.S., L.M.T
Orchard Commons 412 Rte. 9B Larkfield, MA 01999
studio@fernwickmail.com
www.kneadinghavenstudio.com

```html
<!DOCTYPE html>
<html lang="en">
<head>
<meta charset="utf-8">
<title>Kneading Haven Studio – Business Card</title>
<link href="https://fonts.googleapis.com/css2?family=Cormorant+Garamond:wght@500&display=swap" rel="stylesheet">
<style>
  :root {
    --backdrop: #8c8f92;
    --card-blue: #aac4d5;
    --card-white: #fbfbfa;
    --ink-blue: #6f8a9c;
    --ink-deep: #5b7587;
    --emboss: #93b0c3;
  }
  * { box-sizing: border-box; margin: 0; padding: 0; }
  html, body { width: 1200px; height: 908px; overflow: hidden; }
  body {
    background: var(--backdrop);
    font-family: "Cormorant Garamond", Georgia, serif;
    position: relative;
  }
  .card {
    position: absolute;
    top: 304px;
    width: 520px;
    height: 300px;
    border-radius: 22px;
    box-shadow: 0 10px 24px rgba(0,0,0,0.25);
  }
  .card--back { left: 50px; background: var(--card-blue); }
  .card--front { left: 630px; background: var(--card-white); }

  .brand {
    display: flex; align-items: center; gap: 12px;
    font-weight: 500; white-space: nowrap;
  }
  .brand__dot { border-radius: 50%; flex: none; }

  .card--back .brand {
    position: absolute; left: 50%; top: 50%;
    transform: translate(-50%, -50%);
    color: var(--emboss); font-size: 40px;
  }
  .card--back .brand__dot { width: 22px; height: 22px; background: var(--emboss); }

  .card--front .brand {
    position: absolute; left: 40px; top: 72px;
    color: var(--ink-blue); font-size: 24px; gap: 8px;
  }
  .card--front .brand__dot { width: 12px; height: 12px; background: var(--ink-blue); }

  .contact {
    position: absolute; left: 318px; top: 54px;
    color: var(--ink-deep); font-size: 13px; line-height: 18px;
    list-style: none;
  }
  .contact__address { margin-bottom: 8px; }
  .contact__row { display: flex; align-items: center; gap: 6px; }
  .contact__row svg { width: 11px; height: 11px; flex: none; }

  .holder {
    position: absolute; left: 40px; bottom: 42px;
    color: var(--ink-deep); font-size: 19px;
  }
</style>
</head>
<body>
  <section class="card card--back" aria-label="Card back">
    <div class="brand"><span class="brand__dot"></span>Kneading Haven Studio</div>
  </section>

  <section class="card card--front" aria-label="Card front">
    <div class="brand"><span class="brand__dot"></span>Kneading Haven Studio</div>

    <ul class="contact">
      <li class="contact__address">Orchard Commons<br>412 Rte. 9B<br>Larkfield, MA 01999</li>
      <li class="contact__row">
        <svg viewBox="0 0 12 12"><circle cx="6" cy="6" r="6" fill="#6f8a9c"/><path d="M4 3.2l1 1.4-.6.7c.4.9 1 1.5 1.9 1.9l.7-.6 1.4 1-.6 1C5.5 8.4 3.6 6.5 3.4 3.8z" fill="#fff"/></svg>
        508.555.0142
      </li>
      <li class="contact__row">
        <svg viewBox="0 0 12 12"><circle cx="6" cy="6" r="6" fill="#6f8a9c"/><rect x="3" y="4" width="6" height="4.2" fill="none" stroke="#fff" stroke-width=".8"/><path d="M3 4l3 2.3L9 4" fill="none" stroke="#fff" stroke-width=".8"/></svg>
        studio@fernwickmail.com
      </li>
      <li class="contact__row">
        <svg viewBox="0 0 12 12"><circle cx="6" cy="6" r="6" fill="#6f8a9c"/><circle cx="6" cy="6" r="3" fill="none" stroke="#fff" stroke-width=".8"/><path d="M3 6h6M6 3c-1.4 1.6-1.4 4.4 0 6M6 3c1.4 1.6 1.4 4.4 0 6" fill="none" stroke="#fff" stroke-width=".6"/></svg>
        www.kneadinghavenstudio.com
      </li>
      <li class="contact__row">
        <svg viewBox="0 0 12 12"><circle cx="6" cy="6" r="6" fill="#6f8a9c"/></svg>
        GwenH
      </li>
    </ul>

    <p class="holder">Gwen Holloway M.S., L.M.T</p>
  </section>
</body>
</html>
```